Business Consulting Company requires a website design (PSD+HTML+CSS required)

Tarnvale Advisory is a Business Consulting Company that provides Analysis, Business Coaching and Systems and Document Design for clients.

We would like a simplistic yet professional looking website design that uses high quality imagery to project a professional persona across our entire site.

The completed project will need to include PSD files (for editing in Photoshop) and will need to also include HTML+CSS coded files that can be edited in Adobe Dreamweaver CS5.5.

Tarnvale Advisory currently has a functioning website (located at www.tarnvaleadvisory.com.au) but would like to replace its current site with something more professional, user friendly and content simplistic, with the overall design of this project being clean and very easy to navigate whilst remaining professionally focused.

A brief has been attached to this project to provide the key details but please feel free to contact me if you require any clarification or have any questions regarding the project.

Target Market(s)

The target audience for this website will be small to medium sized businesses (of all descriptions).

Industry/Entity Type

Business

Coding

Coded - Design and coding required

Number of Pages Required

5+ page

Requirements
Must have
• Simplistic design structure
• Professional images
• Easy to navigate
• Must be uploaded in PSD format
• Must be coded (HTML+CSS) and compatible with Adobe Dreamweaver CS5.5
Nice to have
• Use of the Company’s corporate colours throughout the site design
• Adding a Home page slider bar with images and short catchy messages (i.e. text based statements)
• Having a quick link box on each page that provides easy navigation throughout the site
• The use of different icons and images to depict our different services (i.e. a different icon and image for analysis service and coaching service etc.).
• All pages should follow a similar theme (universal approach to all pages)
Should not have
• When coding, images should not be used in place of text (all text must be editable)

```html
<!DOCTYPE html>
<html lang="en">
<head>
<meta charset="utf-8">
<title>Tarnvale Advisory</title>
<link rel="stylesheet" href="https://fonts.googleapis.com/css2?family=Questrial&family=Poppins:wght@500;600&display=swap">
<style>
:root{
  --blue:#1a9be0;
  --ink:#141414;
  --text:#555;
  --muted:#888;
  --line:#d9d9d9;
  --grey-bg:#f1f1f1;
  --band:#dce9f4;
  --footer:#f4f4f4;
  --circle:#cfe6f3;
}
*{margin:0;padding:0;box-sizing:border-box}
html,body{width:798px;height:1200px;overflow:hidden;background:#fff}
body{font-family:"Questrial",sans-serif;color:var(--text);position:relative}
.abs{position:absolute}

.topbar{left:0;top:0;width:798px;height:20px;background:#f7f7f7;font-size:7px;color:#666}
.topbar .follow{left:108px;top:5px}
.topbar .follow span{display:inline-block;width:11px;height:11px;border-radius:50%;background:var(--blue);vertical-align:middle;margin-left:2px}
.topbar .addr{left:466px;top:6px}
.topbar .call{left:610px;top:6px}
.topbar svg{vertical-align:middle;margin-right:3px}

.header{left:0;top:20px;width:798px;height:50px;background:#fff}
.brand{display:flex;align-items:center;gap:7px;white-space:nowrap}
.brand .dot{width:20px;height:20px;border-radius:50%;border:2px solid #666}
.brand .name{font-size:17px;color:#666;letter-spacing:.5px}
.header .brand{left:108px;top:14px}
.nav{right:107px;top:22px;display:flex;gap:17px;font-size:8px;color:#666;white-space:nowrap}
.nav .on{color:var(--blue)}
.accent{left:0;top:70px;width:798px;height:3px;background:var(--blue)}

.hero{left:0;top:73px;width:798px;height:299px;background:linear-gradient(90deg,#f4f4f4 0%,#ececec 45%,#e2e4e6 60%,#c9cfd4 100%)}
.hero-photo{left:470px;top:0;width:328px;height:299px;background:radial-gradient(ellipse at 60% 45%,#eef1f3 0%,#cdd3d8 55%,#a9b0b6 100%)}
.hero-copy{left:129px;top:80px}
.hero h1{font-family:"Questrial",sans-serif;font-weight:400;font-size:28px;color:var(--ink);line-height:30px;white-space:nowrap}
.hero h1 .small{font-size:15px;color:#444}
.hero h1 .big{font-family:"Poppins",sans-serif;font-weight:600;font-size:27px;color:var(--blue)}
.hero p{font-size:9.8px;line-height:14px;color:#555;margin-top:4px;width:350px}
.btns{display:flex;gap:5px;margin-top:12px}
.btn{height:25px;display:flex;align-items:center;justify-content:space-between;padding:0 12px 0 14px;font-size:10.5px;color:#fff;white-space:nowrap}
.btn.primary{background:var(--blue);width:101px}
.btn.dark{background:#111;width:102px}
.btn i{width:13px;height:13px;border-radius:50%;border:1px solid rgba(255,255,255,.8);display:inline-block;flex:none}

.welcome{left:0;top:372px;width:798px;height:228px;background:linear-gradient(180deg,#fff 0%,var(--grey-bg) 100%);border-bottom:1px solid #e2e2e2;text-align:center}
.title{font-family:"Poppins",sans-serif;font-weight:600;color:var(--ink);font-size:28px;letter-spacing:-1px}
.divider{width:148px;height:1px;background:var(--line);margin:6px auto 0;position:relative}
.divider::after{content:"";position:absolute;left:69px;top:-5px;width:8px;height:8px;border-radius:50%;border:1.5px solid var(--blue);background:#fff}
.welcome .title{margin-top:30px}
.welcome .sub{font-size:7.5px;color:#777;margin-top:8px}
.welcome .body{width:492px;margin:22px auto 0;font-size:6.6px;line-height:14px;color:#666}
.welcome .more{margin-top:10px;font-size:7.5px;color:#222;display:inline-flex;align-items:center;gap:4px}
.welcome .more i{width:11px;height:11px;border-radius:50%;border:1px solid var(--blue);display:inline-block}

.services{left:0;top:601px;width:798px;height:364px;text-align:center}
.services .title{margin-top:36px}
.svc{position:absolute;width:104px;height:104px;border-radius:50%;display:flex;align-items:center;justify-content:center;text-align:center;font-size:13px;line-height:15px;color:#333}
.svc .bg{position:absolute;inset:0;border-radius:50%;background:radial-gradient(circle at 40% 35%,#e6f2f9,var(--circle))}
.svc span{position:relative;white-space:nowrap}
.svc.deep .bg{background:radial-gradient(circle at 40% 35%,#5fb3dc,#2a8cc0)}
.svc.deep{color:#fff}
.arrow{position:absolute;top:190px}

.testimonial{left:0;top:965px;width:798px;height:122px;background:var(--band)}
.avatar{left:166px;top:23px;width:57px;height:57px;border-radius:50%;border:3px solid #fff;background:radial-gradient(circle,#e9c3a3,#c98e6a)}
.who{left:140px;top:85px;width:110px;text-align:center;font-size:7.5px;color:#333;line-height:10px}
.who small{display:block;font-size:6px;font-family:"Poppins",sans-serif}
.quote{left:238px;top:26px;width:400px;font-size:10.5px;line-height:15px;color:#555}
.qmark{font-family:"Poppins",sans-serif;font-size:20px;color:#bbb;line-height:10px}
.date{left:565px;top:86px;font-size:7.5px;color:#333}

.footer{left:0;top:1087px;width:798px;height:113px;background:var(--footer)}
.footer .brand{left:108px;top:27px}
.legal{left:108px;top:65px;font-size:7px;color:#555;line-height:10px}
.col{top:28px;font-size:7px;color:#888;width:200px}
.col h4{font-family:"Poppins",sans-serif;font-weight:500;font-size:7.5px;color:#222;margin-bottom:8px}
.col .row{display:flex;gap:6px;margin-bottom:6px;line-height:9px}
.col .row svg{flex:none}
</style>
</head>
<body>

<div class="abs topbar">
  <div class="abs follow">Follow us on: <span></span><span></span></div>
  <div class="abs addr"><svg width="8" height="9" viewBox="0 0 8 10"><path d="M4 9.5C2 7 1 5.5 1 4a3 3 0 016 0c0 1.5-1 3-3 5.5z" fill="none" stroke="#1a9be0"/></svg>48 Kelso Lane, Level 2</div>
  <div class="abs call"><svg width="9" height="9" viewBox="0 0 10 10"><path d="M2 1l2 2-1 1.5a6 6 0 002.5 2.5L7 6l2 2-1.5 1.5C4.5 9 1 5.5.5 2.5z" fill="none" stroke="#1a9be0"/></svg>Call Us: 03 62 18 4417</div>
</div>

<header class="abs header">
  <div class="abs brand"><div class="dot"></div><div class="name">Tarnvale Advisory</div></div>
  <nav class="abs nav"><span class="on">Home</span><span>Why Tarnvale?</span><span>Our Services</span><span>Products</span><span>Delivery Method</span><span>Contact</span><span>Blog</span></nav>
</header>
<div class="abs accent"></div>

<section class="abs hero">
  <div class="abs hero-photo" role="img" aria-label="Overhead view of business people meeting around a glass table in white armchairs"></div>
  <div class="abs hero-copy">
    <h1>We Take The Pain<br><span class="small">Out Of </span><span class="big">Doing Bussiness</span></h1>
    <p>Tarnvale Advisory is a Business Development and Consulting Company that provides affordable, high quality business solutions that are...</p>
    <div class="btns"><div class="btn primary"><span>Read More</span><i></i></div><div class="btn dark"><span>Contact Us</span><i></i></div></div>
  </div>
</section>

<section class="abs welcome">
  <h2 class="title">Welcome To</h2>
  <div class="divider"></div>
  <div class="sub">Tarnvale Advisory</div>
  <p class="body">Tarnvale Advisory is a Business Development and Consulting Company that provides affordable, high quality business solutions that are easy to understand and that are individually tailored to suit the needs of our clients.Understanding that each of our clients businesses are unique, Tarnvale works closely with our business partners to ensure the correct solutions are in place and that optimum efficiency is achieved.We focus on delivering immediate wins to guarantee value for money, all the while securing the transfer of essential skills and knowledge into the business, safeguarding a successful future for our clients.</p>
  <div class="more">Read more <i></i></div>
</section>

<section class="abs services">
  <h2 class="title">Our Services</h2>
  <div class="divider"></div>
  <svg class="arrow" style="left:74px" width="22" height="42" viewBox="0 0 22 42"><path d="M21 1L1 21l20 20" fill="none" stroke="#ddd" stroke-width="1.2"/></svg>
  <svg class="arrow" style="left:702px" width="22" height="42" viewBox="0 0 22 42"><path d="M1 1l20 20L1 41" fill="none" stroke="#ddd" stroke-width="1.2"/></svg>
  <div class="svc" style="left:201px;top:129px"><div class="bg" role="img" aria-label="Faint mind map of advertising planning terms"></div><span>Advertising<br>Strategies</span></div>
  <div class="svc" style="left:346px;top:132px"><div class="bg" role="img" aria-label="Faint strategy chart"></div><span>Growth<br>Strategies</span></div>
  <div class="svc" style="left:490px;top:132px"><div class="bg" role="img" aria-label="Business planning on a desk"></div><span>Business<br>planning</span></div>
  <div class="svc deep" style="left:125px;top:213px"><div class="bg" role="img" aria-label="Businessman climbing upward on a blue background"></div><span>Increasing<br>Profitability</span></div>
  <div class="svc" style="left:272px;top:214px"><div class="bg" role="img" aria-label="Hands working on a tablet"></div><span>Creation &amp;<br>implement</span></div>
  <div class="svc" style="left:417px;top:215px"><div class="bg" role="img" aria-label="Person writing at a laptop"></div><span>Business &amp;<br>Product</span></div>
  <div class="svc" style="left:570px;top:206px"><div class="bg" role="img" aria-label="Process diagram with a magnifying glass"></div><span>Process &amp; work<br>flow mapping</span></div>
</section>

<section class="abs testimonial">
  <div class="abs avatar" role="img" aria-label="Portrait of the client"></div>
  <div class="abs who">– Nora Whitcombe<small>Director Corvell Pty Ltd.</small></div>
  <p class="abs quote"><span class="qmark">&ldquo;</span>Daniel has been instrumental in my professional development. I was a worker bee with leadership potential I was a worker bee with leadership potential I was a worker bee withthe confidence to make the transition from a worker to a leader<span class="qmark">&rdquo;</span></p>
  <div class="abs date">10-Monday-2014</div>
</section>

<footer class="abs footer">
  <div class="abs brand"><div class="dot"></div><div class="name">Tarnvale Advisory</div></div>
  <div class="abs legal">Copyrights © 2014 TarnvaleAdvisory<br>Terms &amp; Conditions &nbsp;|&nbsp; Privacy Policy</div>
  <div class="abs col" style="left:316px">
    <h4>Tarnvale-Advisory Address #1</h4>
    <div class="row"><svg width="8" height="10" viewBox="0 0 8 10"><path d="M4 9.5C2 7 1 5.5 1 4a3 3 0 016 0c0 1.5-1 3-3 5.5z" fill="#bbb"/></svg><span>PO Box: 4720, Moorfield, Victoria,<br>Australia 3912</span></div>
    <div class="row"><svg width="8" height="10" viewBox="0 0 8 10"><path d="M3 0.5h3v2H4.5a5 5 0 000 5H6v2H3C1 8 1 2 3 .5z" fill="#bbb"/></svg><span>Office: 03 6218 4417</span></div>
    <div class="row"><svg width="9" height="7" viewBox="0 0 9 7"><rect width="9" height="7" fill="#bbb"/><path d="M0 0l4.5 4L9 0" fill="none" stroke="#fff"/></svg><span>Email: admin@tarnvaleadvisory.com.au</span></div>
  </div>
  <div class="abs col" style="left:533px">
    <h4>Tarnvale-Advisory Address #2</h4>
    <div class="row"><svg width="8" height="10" viewBox="0 0 8 10"><path d="M4 9.5C2 7 1 5.5 1 4a3 3 0 016 0c0 1.5-1 3-3 5.5z" fill="#bbb"/></svg><span>PO Box: 4720, Moorfield, Victoria,<br>Australia 3912</span></div>
    <div class="row"><svg width="8" height="10" viewBox="0 0 8 10"><path d="M3 0.5h3v2H4.5a5 5 0 000 5H6v2H3C1 8 1 2 3 .5z" fill="#bbb"/></svg><span>Office: 03 6218 4417</span></div>
    <div class="row"><svg width="9" height="7" viewBox="0 0 9 7"><rect width="9" height="7" fill="#bbb"/><path d="M0 0l4.5 4L9 0" fill="none" stroke="#fff"/></svg><span>Email: admin@tarnvaleadvisory.com.au</span></div>
  </div>
</footer>

</body>
</html>
```